BRIGHTHOLM ADVISORY powerpoint deck.

I REQUIRE A COMPANY POWERPOINT SLIDE DECK, WHICH MAY ALSO INCLUDE A NUMBER OF "MODELS". THIS MAY ALSO REQUIRE SOME FOLLOW UP WORK.

ATTACHED IS AN EXAMPLE SLIDE DECK FOR ONE OF MY CLIENTS. I would like to see a mock up of a few slides and then i can send a complete deck over.

Please note my website... www.brightholmadvisory.co.uk

I LOOK FORWARD TO SEEING YOUR DESIGN.

THANK YOU,

DAVID.

I work in the "learning and development"/ education/ leadership/ coaching industry

Leadership

Other font styles liked:
• century gothic

• ideally there would be some alignment to my website. www.brightholmadvisory.co.uk
• be fresh, clean, simple enough. look professional.
• how you present "models" i would come back for more work in the future if the work is good.
• too brash.

```html
<!DOCTYPE html>
<html lang="en">
<head>
<meta charset="utf-8">
<title>High Level Leadership development objectives – Brightholm Advisory</title>
<link href="https://fonts.googleapis.com/css2?family=Mulish:wght@400;700&display=swap" rel="stylesheet">
<style>
  :root {
    --teal: #3b9690;
    --teal-dark: #1f5c4f;
    --text-grey: #6d6e70;
    --footer-grey: #808383;
    --logo-panel: #f2f4f4;
    --logo-ink: #3a3d3d;
    --white: #ffffff;
  }
  * { margin: 0; padding: 0; box-sizing: border-box; }
  html, body { width: 1200px; height: 900px; overflow: hidden; background: var(--white); }
  .slide {
    position: relative;
    width: 1200px;
    height: 900px;
    background: var(--white);
    font-family: "Mulish", "Century Gothic", sans-serif;
    overflow: hidden;
  }
  .title-band {
    position: absolute;
    left: 0; top: 0;
    width: 1200px; height: 102px;
    background: var(--teal);
  }
  .slide-title {
    position: absolute;
    left: 30px; top: 30px;
    color: var(--white);
    font-weight: 700;
    font-size: 33px;
    letter-spacing: 0.2px;
  }
  .brand-tab {
    position: absolute;
    left: 915px; top: 0;
    width: 234px; height: 156px;
  }
  .brand-name {
    position: absolute;
    left: 915px; top: 48px;
    width: 234px;
    text-align: center;
    color: var(--logo-ink);
    font-weight: 700;
    font-size: 17px;
    line-height: 22px;
    letter-spacing: 1.5px;
  }
  .brand-dot {
    display: block;
    width: 14px; height: 14px;
    border-radius: 50%;
    background: var(--teal);
    margin: 0 auto 8px;
  }
  .objectives { list-style: none; }
  .objective {
    position: absolute;
    left: 90px;
    width: 1080px;
    color: var(--text-grey);
    font-size: 25px;
    line-height: 39px;
  }
  .objective-marker {
    position: absolute;
    left: -69px; top: 3px;
    width: 51px; height: 33px;
  }
  .footer-band {
    position: absolute;
    left: 0; bottom: 0;
    width: 1200px; height: 35px;
    background: var(--footer-grey);
  }
</style>
</head>
<body>
<div class="slide">
  <header>
    <div class="title-band"></div>
    <h1 class="slide-title">High Level Leadership development objectives</h1>
    <svg class="brand-tab" viewBox="0 0 234 156" aria-hidden="true">
      <polygon points="0,0 234,0 234,110 117,156 0,110" fill="var(--logo-panel)"/>
    </svg>
    <div class="brand-name"><span class="brand-dot"></span>BRIGHTHOLM<br>ADVISORY</div>
  </header>

  <ul class="objectives">
    <li class="objective" style="top:162px">
      <svg class="objective-marker" viewBox="0 0 51 33" aria-hidden="true"><polygon points="0,0 38,0 51,16.5 38,33 0,33 8,16.5" fill="var(--teal)"/><circle cx="29" cy="16.5" r="8" fill="var(--teal-dark)"/></svg>
      Leadership is about responsibility not authority. Develop a sense of “I represent the whole company/team”, develop a sense of company pride and increase safety standards.
    </li>
    <li class="objective" style="top:310px">
      <svg class="objective-marker" viewBox="0 0 51 33" aria-hidden="true"><polygon points="0,0 38,0 51,16.5 38,33 0,33 8,16.5" fill="var(--teal)"/><circle cx="29" cy="16.5" r="8" fill="var(--teal-dark)"/></svg>
      Embed the “Northpoint Way” culture and identity throughout the business.
    </li>
    <li class="objective" style="top:385px">
      <svg class="objective-marker" viewBox="0 0 51 33" aria-hidden="true"><polygon points="0,0 38,0 51,16.5 38,33 0,33 8,16.5" fill="var(--teal)"/><circle cx="29" cy="16.5" r="8" fill="var(--teal-dark)"/></svg>
      Fundamentally develop leadership and coaching skills throughout the business.
    </li>
    <li class="objective" style="top:456px">
      <svg class="objective-marker" viewBox="0 0 51 33" aria-hidden="true"><polygon points="0,0 38,0 51,16.5 38,33 0,33 8,16.5" fill="var(--teal)"/><circle cx="29" cy="16.5" r="8" fill="var(--teal-dark)"/></svg>
      Identify people for the future. Develop a leadership pipeline.
    </li>
    <li class="objective" style="top:528px">
      <svg class="objective-marker" viewBox="0 0 51 33" aria-hidden="true"><polygon points="0,0 38,0 51,16.5 38,33 0,33 8,16.5" fill="var(--teal)"/><circle cx="29" cy="16.5" r="8" fill="var(--teal-dark)"/></svg>
      Planning skills, development of consistent SOPs, effective communication skills, simplify to improve efficiency.
    </li>
    <li class="objective" style="top:634px">
      <svg class="objective-marker" viewBox="0 0 51 33" aria-hidden="true"><polygon points="0,0 38,0 51,16.5 38,33 0,33 8,16.5" fill="var(--teal)"/><circle cx="29" cy="16.5" r="8" fill="var(--teal-dark)"/></svg>
      For all levels of the business to embrace change: it isn’t just TM anymore.
    </li>
    <li class="objective" style="top:720px">
      <svg class="objective-marker" viewBox="0 0 51 33" aria-hidden="true"><polygon points="0,0 38,0 51,16.5 38,33 0,33 8,16.5" fill="var(--teal)"/><circle cx="29" cy="16.5" r="8" fill="var(--teal-dark)"/></svg>
      Client relationships are critical, see it from client’s perspective, have a strong customer focus.
    </li>
  </ul>

  <footer class="footer-band"></footer>
</div>
</body>
</html>
```